Business Card Design Project

Business Card
We are rebranding with a new logo
Industry/Entity Type
Business
Contact Information for Business Card
Dennis Marlow +61 427581962 dennis@qovo.com.au P.O. Box 872 Kelvindale QLD 4309
Requirements
Must have
- Logo

```html
<!DOCTYPE html>
<html lang="en">
<head>
<meta charset="UTF-8">
<title>Qovo International – Business Card</title>
<link rel="stylesheet" href="https://fonts.googleapis.com/css2?family=Fira+Sans+Condensed:wght@700&family=Montserrat:wght@300;400;700&display=swap">
<style>
  :root {
    --page-bg: #e3e4e6;
    --card-bg: #ffffff;
    --navy: #02506f;
    --ocean: #0077a8;
    --sky: #18a6de;
    --rust: #e8662a;
    --amber: #f58d22;
    --teal-deep: #065a7d;
    --panel-light: #00a0e2;
    --panel-dark: #004a80;
    --ink: #222226;
    --white: #ffffff;
  }
  * { margin: 0; padding: 0; box-sizing: border-box; }
  html, body {
    width: 1200px;
    height: 1200px;
    overflow: hidden;
    background: var(--page-bg);
  }
  .card {
    position: absolute;
    left: 52px;
    top: 287px;
    width: 1096px;
    height: 625px;
    background: var(--card-bg);
    overflow: hidden;
    font-family: "Montserrat", sans-serif;
  }
  .card__stripes,
  .card__panel,
  .card__slashes {
    position: absolute;
    left: 0;
    top: 0;
  }
  .brand {
    position: absolute;
    left: 68px;
    top: 180px;
    width: 390px;
    color: var(--ocean);
    font-family: "Montserrat", sans-serif;
    font-weight: 700;
    text-align: center;
    line-height: 1;
  }
  .brand__name {
    display: block;
    font-size: 104px;
    letter-spacing: 2px;
  }
  .brand__tagline {
    display: block;
    margin-top: 18px;
    font-size: 31px;
    letter-spacing: 4px;
  }
  .contact-name {
    position: absolute;
    left: 640px;
    top: 183px;
    width: 406px;
    height: 75px;
    border: 1px solid rgba(255,255,255,0.85);
    color: var(--white);
    font-family: "Fira Sans Condensed", sans-serif;
    font-weight: 700;
    font-size: 46px;
    letter-spacing: 3px;
    text-align: center;
    line-height: 73px;
  }
  .contact-phone {
    position: absolute;
    left: 620px;
    top: 278px;
    width: 446px;
    color: var(--white);
    font-weight: 700;
    font-size: 37px;
    text-align: center;
    letter-spacing: 0.5px;
  }
  .address {
    position: absolute;
    left: 180px;
    top: 480px;
    width: 736px;
    text-align: center;
    color: var(--ink);
    font-size: 34px;
    line-height: 1.5;
  }
  .address__line {
    display: block;
    font-weight: 400;
    letter-spacing: 1.5px;
  }
  .address__email {
    display: block;
    font-weight: 700;
    letter-spacing: 1px;
  }
  .address__at { color: var(--amber); }
</style>
</head>
<body>
  <div class="card">
    <svg class="card__stripes" width="1096" height="45" viewBox="0 0 1096 45">
      <rect x="0" y="0" width="1096" height="45" fill="var(--teal-deep)"/>
      <polygon points="0,0 200,0 188,45 0,45" fill="var(--navy)"/>
      <polygon points="200,0 398,0 386,45 188,45" fill="var(--ocean)"/>
      <polygon points="398,0 596,0 584,45 386,45" fill="var(--sky)"/>
      <polygon points="596,0 796,0 784,45 584,45" fill="var(--rust)"/>
      <polygon points="796,0 994,0 982,45 784,45" fill="var(--amber)"/>
    </svg>

    <svg class="card__panel" width="1096" height="625" viewBox="0 0 1096 625">
      <defs>
        <linearGradient id="panelGradient" x1="0" y1="0" x2="1" y2="0">
          <stop offset="0.1" stop-color="var(--panel-light)"/>
          <stop offset="1" stop-color="var(--panel-dark)"/>
        </linearGradient>
      </defs>
      <path d="M600 88 H1096 V417 H680 Q610 417 585 360 L514 185 Q492 88 600 88 Z" fill="url(#panelGradient)"/>
    </svg>

    <div class="brand">
      <span class="brand__name">Qovo</span>
      <span class="brand__tagline">INTERNATIONAL</span>
    </div>

    <div class="contact-name">DENNIS MARLOW</div>
    <div class="contact-phone">Ph: +61 427581962</div>

    <svg class="card__slashes" width="1096" height="625" viewBox="0 0 1096 625">
      <line x1="164" y1="483" x2="198" y2="572" stroke="var(--amber)" stroke-width="4"/>
      <line x1="898" y1="474" x2="932" y2="563" stroke="var(--amber)" stroke-width="4"/>
    </svg>

    <div class="address">
      <span class="address__line">P.O. Box - 872, Kelvindale, QLD - 4309</span>
      <span class="address__email">dennis<span class="address__at">@</span>qovo.com.au</span>
    </div>
  </div>
</body>
</html>
```